Web Design Project - (DESIGN AND FOLLOW UP CODING)

Web design for new management consultancy company

**About The Hadley Collective

We work with organisations find and implement creative and sensible solutions...

We explore and inform…We have in-house research capability and enrich discussion through our own research, analysis and inputs. We interview staff and stakeholders, analyse data and literature and help you develop knowledge and solutions, and the plans to implement these.

We present new ideas…We develop proposals and reports that use internally and externally derived evidence to propose effective new solutions.

Specialties
Higher Education, TAFE, Local Government, Regional Development

Industry
Education Management
Updates

LOGO added to brief (or email me on mavenlink@quorix.com.au to get copy

Target Market(s)

Business and government managers

Industry/Entity Type

Education

Requirements
Must have
• Sections:

**About
We work with organisations find and implement solutions to opportunities and challenges.
We explore and inform…
We present new ideas…

We develop proposals and reports that link internally and externally derived evidence to develop and implement new solutions.

Our three practice pillars are-
Ideas and partnerships:
Knowledgeable leaders:
Solutions:

** People
Marcus Pellow (PHOTO) Bio

** Services
Acumen - Solutions - Partnerships -Implementation
- On time and within budget.
- Project leadership.
- Researched inputs and facilitated outcomes.
- Focus on implementation.
- Develop value-adding partnerships and get them funded
- Creative responses to funding opportunities
- Organisational reviews

Sectors
-Education
-State Government
- Local Government
- Utilities
- Financial services
- Health and ageing
- Human services
- Government
-Regional

** Careers

** Key Partners
With weblinks

** Contact

Links to Twitter LinkedIn Facebook
Nice to have
• Logo available from: mavenlink@quorix.com.au

```html
<!DOCTYPE html>
<html lang="en">
<head>
<meta charset="utf-8">
<title>The Hadley Collective – Home</title>
<link rel="stylesheet" href="https://fonts.googleapis.com/css2?family=Questrial&family=Crimson+Text:ital@1&display=swap">
<style>
  :root {
    --sky: #aed4e0;
    --mist: #c9c9c9;
    --teal: #0b5f7f;
    --teal-text: #0d6786;
    --navy: #014a6e;
    --nav-top: #0d6a94;
    --nav-idle: #a9d3e4;
    --accent: #f0682c;
    --white: #ffffff;
    --sans: "Questrial", "Century Gothic", sans-serif;
  }
  * { box-sizing: border-box; margin: 0; padding: 0; }
  html, body { width: 1200px; height: 1000px; overflow: hidden; }
  body { position: relative; font-family: var(--sans); color: var(--teal-text);
    background: linear-gradient(180deg, var(--sky) 0%, var(--sky) 14%, var(--mist) 30%, var(--mist) 75%, var(--sky) 92%); }

  .utility-links { position: absolute; top: 4px; right: 123px; font-size: 16px; color: var(--teal); }
  .utility-links span { margin: 0 6px; }

  .brand { position: absolute; left: 120px; top: 26px; }
  .brand-name { display: flex; align-items: center; gap: 12px; font-size: 40px; color: var(--teal); letter-spacing: -0.3px; line-height: 1; }
  .brand-mark { width: 22px; height: 22px; background: var(--accent); }
  .brand-pillars { margin: 6px 0 0 34px; font-size: 18px; line-height: 20px; font-weight: 700; color: var(--accent); white-space: nowrap; }
  .brand-intro { position: absolute; left: 121px; top: 95px; width: 540px; font-size: 14px; line-height: 15px; font-style: italic; color: var(--teal); }

  .search { position: absolute; left: 892px; top: 83px; width: 185px; height: 31px; background: var(--white); border: 1px solid #8a8a8a; display: flex; align-items: center; padding-left: 4px; gap: 10px; font-size: 15px; color: #7c7c7c; }

  .main-nav { position: absolute; left: 120px; top: 136px; width: 960px; height: 56px; background: linear-gradient(var(--nav-top), var(--navy)); display: flex; align-items: center; justify-content: space-between; padding: 0 19px 0 21px; }
  .main-nav a { text-decoration: none; color: var(--nav-idle); font-size: 24px; font-weight: 700; letter-spacing: 0.3px; }
  .main-nav a.current { color: var(--white); }

  .hero { position: absolute; left: 120px; top: 197px; width: 960px; height: 484px; background: linear-gradient(100deg, #d8d4cf 0%, #bfb7ad 35%, #cfcdc8 60%, #a9a7a3 100%); }
  .hero-caption { position: absolute; left: 0; bottom: 0; width: 100%; height: 94px; background: rgba(10,10,10,0.62); text-align: center; }
  .hero-caption q { display: block; margin-top: 14px; font-family: "Crimson Text", Georgia, serif; font-style: italic; font-size: 24px; color: var(--white); }
  .hero-dots { display: flex; justify-content: center; gap: 5px; margin-top: 8px; }
  .hero-dots span { width: 15px; height: 15px; border-radius: 50%; border: 2px solid #d8d8d8; }
  .hero-dots span.active { background: #bdbdbd; }

  .panel { position: absolute; background: var(--white); border: 3px solid var(--teal); }
  .panel h2 { font-weight: 400; font-size: 33px; color: var(--teal); line-height: 1; }
  .panel p { font-size: 17.5px; line-height: 19px; text-align: justify; text-indent: 30px; color: var(--teal-text); }
  .news { left: 121px; top: 698px; width: 291px; height: 177px; padding: 9px 12px 0 13px; }
  .news h2 { margin-bottom: 21px; }
  .see-more { display: block; text-align: right; font-size: 15px; margin-top: 4px; color: var(--teal); text-decoration: none; }
  .side-note { left: 121px; top: 894px; width: 291px; height: 130px; padding: 9px 12px 0 13px; }
  .side-note h2 { margin-bottom: 18px; }
  .welcome { left: 441px; top: 698px; width: 637px; height: 330px; padding: 9px 12px 0 9px; }
  .welcome h2 { margin-bottom: 22px; }
  .welcome p { margin-bottom: 19px; }
</style>
</head>
<body>
  <nav class="utility-links">FAQs<span>|</span>Help<span>|</span>Optional Links</nav>

  <header class="brand">
    <div class="brand-name"><span class="brand-mark"></span>The Hadley Collective</div>
    <p class="brand-pillars">Acumen - Solutions - Partnerships - Implementation</p>
  </header>
  <p class="brand-intro">We present new ideas…We develop proposals and reports that use internally and externally derived evidence to propose effective new solutions.</p>

  <div class="search">
    <svg width="26" height="26" viewBox="0 0 26 26" aria-hidden="true"><circle cx="10" cy="10" r="7.5" fill="#eef3f7" stroke="#6a7b8a" stroke-width="2"/><line x1="15.5" y1="15.5" x2="23" y2="23" stroke="#4d5b66" stroke-width="3.5" stroke-linecap="round"/></svg>
    Search here...
  </div>

  <nav class="main-nav">
    <a class="current" href="#">HOME</a>
    <a href="#">ABOUT US</a>
    <a href="#">PEOPLE</a>
    <a href="#">SERVICES</a>
    <a href="#">CAREERS</a>
    <a href="#">PARTNERS</a>
    <a href="#">CONTACT US</a>
  </nav>

  <section class="hero" role="img" aria-label="Photo of two colleagues reviewing documents at a laptop in a busy office">
    <div class="hero-caption">
      <q>We explore and inform…</q>
      <div class="hero-dots"><span class="active"></span><span></span><span></span><span></span><span></span></div>
    </div>
  </section>

  <section class="panel news">
    <h2>News</h2>
    <p>Dummy Text. Maybe some recent news or projects will be placed here. Or somewhing can be placed here</p>
    <a class="see-more" href="#">see more...</a>
  </section>

  <section class="panel side-note">
    <h2>Headings #1</h2>
    <p>Dummy Text. Maybe some recent news or projects will be placed here. Or something can</p>
  </section>

  <section class="panel welcome">
    <h2>Welcome</h2>
    <p>Dummy Text. We work with organisations find and implement creative and sensible solutions...</p>
    <p>We explore and inform…We have in-house research capability and enrich discussion through our own research, analysis and inputs. We interview staff and stakeholders, analyse data and literature and help you develop knowledge and solutions, and the plans to implement these.</p>
    <p>We present new ideas…We develop proposals and reports that use internally and externally derived evidence to propose effective new solutions.</p>
  </section>
</body>
</html>
```